Bright, Fun and hard to forget home inspection business card.

We need a Business card design for a new Home Inspection company. We are building a brand that is bright, fun and easy to remember.

Target Market(s)

Anyone involed in buying and selling of homes.

Industry/Entity Type

Home Inspection

Contact Information for Business Card

Colin Marlowe Owner/Inspector

Wedsite- PorchAndRafterCheck.example
Phone: 253-555-0187
Email- ColinMarlowe@mailbox.example
WA Lic # 4806

Requirements
Must have
• BRQV LOGO somewhere on card.

```html
<!DOCTYPE html>
<html lang="en">
<head>
<meta charset="utf-8">
<title>Porch &amp; Rafter Check — Business Card</title>
<link href="https://fonts.googleapis.com/css2?family=Lato:wght@400;700;900&display=swap" rel="stylesheet">
<style>
  :root {
    --ink: #231f20;
    --orange: #f15a24;
    --white: #ffffff;
    --stage: #d9d9d9;
    --badge-red: #d6202f;
  }
  * { box-sizing: border-box; margin: 0; padding: 0; }
  html, body { width: 1200px; height: 926px; overflow: hidden; }
  body {
    background: var(--stage);
    font-family: "Lato", sans-serif;
    position: relative;
  }
  .card {
    position: absolute;
    left: 230px;
    width: 740px;
    height: 423px;
    background: var(--ink);
    border-radius: 4px;
    overflow: hidden;
    color: var(--white);
  }
  .card--back { top: 25px; }
  .card--front { top: 478px; }

  /* Back side: brand mark */
  .brand-lockup {
    position: absolute;
    inset: 0;
    display: flex;
    align-items: center;
    justify-content: center;
    gap: 26px;
  }
  .brand-dot {
    width: 96px; height: 96px;
    border-radius: 50%;
    background: var(--orange);
    flex: none;
  }
  .brand-name {
    font-weight: 900;
    font-size: 52px;
    line-height: 1.02;
    text-transform: uppercase;
    color: var(--white);
  }

  /* Front side */
  .wave { position: absolute; inset: 0; width: 100%; height: 100%; }
  .brand-small {
    position: absolute;
    left: 36px; top: 40px;
    display: flex; align-items: center; gap: 12px;
  }
  .brand-small .brand-dot { width: 44px; height: 44px; }
  .brand-small .brand-name { font-size: 22px; }

  .person {
    position: absolute;
    left: 470px; top: 112px;
    text-align: center;
  }
  .person-name { font-weight: 700; font-size: 30px; }
  .person-role { font-size: 17px; margin-top: 2px; }

  .contacts {
    position: absolute;
    left: 34px; top: 292px;
    list-style: none;
    font-size: 19px;
    line-height: 30px;
  }
  .contacts li { display: flex; align-items: center; gap: 8px; }
  .contacts svg { width: 18px; height: 18px; flex: none; }

  .cert-badge {
    position: absolute;
    left: 505px; top: 250px;
    width: 112px; height: 112px;
    background: var(--white);
    border: 6px solid var(--ink);
  }
  .cert-badge::after {
    content: "";
    position: absolute;
    left: 28px; top: 22px;
    width: 44px; height: 44px;
    border-radius: 50%;
    background: var(--badge-red);
  }
  .license {
    position: absolute;
    left: 480px; top: 372px;
    width: 162px;
    text-align: center;
    font-weight: 700;
    font-size: 20px;
  }
</style>
</head>
<body>

<section class="card card--back" aria-label="Card back">
  <div class="brand-lockup">
    <span class="brand-dot"></span>
    <span class="brand-name">Porch &amp; Rafter<br>Check LLC</span>
  </div>
</section>

<section class="card card--front" aria-label="Card front">
  <svg class="wave" viewBox="0 0 740 423" preserveAspectRatio="none" aria-hidden="true">
    <path d="M0 215 C150 180 300 200 420 240 C540 280 640 250 740 200 L740 423 L0 423 Z" fill="var(--orange)"/>
  </svg>

  <div class="brand-small">
    <span class="brand-dot"></span>
    <span class="brand-name">Porch &amp; Rafter<br>Check LLC</span>
  </div>

  <div class="person">
    <p class="person-name">Colin Marlowe</p>
    <p class="person-role">Owner/Inspector</p>
  </div>

  <ul class="contacts">
    <li>
      <svg viewBox="0 0 20 20" aria-hidden="true"><rect width="20" height="20" rx="4" fill="var(--white)"/><path d="M6 4 L8 4 L9 7 L7.5 8.5 C8.5 10.5 9.5 11.5 11.5 12.5 L13 11 L16 12 L16 14 C16 15 15 16 14 16 C8.5 15.5 4.5 11.5 4 6 C4 5 5 4 6 4 Z" fill="var(--ink)"/></svg>
      253-555-0187
    </li>
    <li>
      <svg viewBox="0 0 20 20" aria-hidden="true"><rect width="20" height="20" rx="4" fill="var(--white)"/><rect x="4" y="6" width="12" height="8" fill="var(--ink)"/><path d="M4 6 L10 11 L16 6" stroke="var(--white)" stroke-width="1.2" fill="none"/></svg>
      ColinMarlowe@mailbox.example
    </li>
    <li>
      <svg viewBox="0 0 20 20" aria-hidden="true"><rect width="20" height="20" rx="4" fill="var(--white)"/><circle cx="10" cy="10" r="6" fill="none" stroke="var(--ink)" stroke-width="1.5"/><path d="M4 10 H16 M10 4 C7 7 7 13 10 16 M10 4 C13 7 13 13 10 16" stroke="var(--ink)" stroke-width="1.2" fill="none"/></svg>
      www.PorchAndRafterCheck.example
    </li>
  </ul>

  <div class="cert-badge" role="img" aria-label="Inspector certification badge"></div>
  <p class="license">WA Lic # 4806</p>
</section>

</body>
</html>
```